Web 2.0 my 1 page website ($500 Guaranteed)

Im looking for someone who can update my existing design at http://www.lorwenbastable.com
I like existing layout and the way the boxes all work. Looking for the same design but with an updated web 2.0 textured look and feel.
Please note the current site is already working on top of wordpress and new design needs to also work with wordpress so I can continue to page content.
Looking for designer who can also get it working in wordpress as it is today.
$500 AUD first prize for it all working.
If it helps:
I like minimailist. I like white. I like bright. I like texture. I like backgrounds. I like horizontal stripes running the length of the page. I like designs that work regardless of width of page. I like big bold statements. I like obvious. I like round edges. I like sites that look like they have come alive. I like depth. I like a 3D look. I like something very subtle that moves occassionally - just enough to catch your eye. I dont like popups. I dont like scrolling.
I like really clean SEO friendly source code. I like standards compatible design.
http://www.dovetrunk.ie/ I like the depth of the mini coming out of the screen. I like the big bold fonts and the bright colours. I like the horizontal red stripe running the length of the page.
http://www.quillmoor.ie/ I like the backround clouds. I like the nice big lettering on the font on the mene bar. I like the nice bog boxes and contact numbers.
http://www.kuusilampola.fi/ I like the bright colours on the phone. I like the splash of the bubbles at the top of the page.
http://plumtidewax.me/ I like the blurred background. I REALLY like the rounded enter your email and notify me text boxes. I like the fonts on notify me and the textured background of the button.
http://9rpod.com/it/ I really like the horizontal bar across the page - I like the big fonts in this background - I like the green and the orange. I really like the depth - how the beans and chair and butterfly sit on top of the page kind of bringing it to life. Like all the layers giving that illusion of 3D.
http://www.ferrisdunbolt.net/ Like the big fonts, the horizontal bar, the leather stitching look around the "lets work together" and how everything is shadowed and sits off the page. I like the big contact us / get in touch / fonts at the bottom the big social media buttons. Probably this area could all be half the size but I like it.
http://www.grovinks.com/ I like the graining textures in the background grays. I prefer blues and whites.
http://tevirdalecrates.ca/ Like the big bold texts and the colours. Like the 3D cardboard box coming off the page.
http://puddlebeacon.com/ Like the textured backround - the rough grainy blue.
http://www.qo-rt.com/ I always liked those background kind of bursts behind the bay area picture in the middle. Like the striped blue background.
http://workshop.movrastel.com/ Who doesnt like a ninja, but again like the big fonts and the way the person has depth
http://www.pebblefoxes.com/ I like the depth. I like the big bold colours.
http://www.5kelvra.com/ Again like how the product is featured with lighting behind it, has that 3D look. Nice big lettering etc.
Updates
I like minimailist. I like white. I like bright. I like texture. I like
backgrounds. I like horizontal stripes running the length of the page. I
like designs that work regardless of width of page. I like big bold
statements. I like obvious. I like round edges. I like sites that look
like they have come alive. I like depth. I like a 3D look. I like
something very subtle that moves occassionally - just enough to catch
your eye. I dont like popups. I dont like scrolling.
http://www.dovetrunk.ie/
I like the depth of the mini coming out of the screen. I like the big
bold fonts and the bright colours. I like the horizontal red stripe
running the length of the page.
http://www.quillmoor.ie/
I like the backround clouds. I like the nice big lettering on the font
on the mene bar. I like the nice bog boxes and contact numbers.
http://plumtidewax.me/
I like the blurred background. I REALLY like the rounded enter your
email and notify me text boxes. I like the fonts on notify me and the
textured background of the button.
http://9rpod.com/it/
I really like the horizontal bar across the page - I like the big fonts
in this background - I like the green and the orange. I really like the
depth - how the beans and chair and butterfly sit on top of the page
kind of bringing it to life. Like all the layers giving that illusion of
3D.
http://www.ferrisdunbolt.net/
Like the big fonts, the horizontal bar, the leather stitching look
around the "lets work together" and how everything is shadowed and sits
off the page. I like the big contact us / get in touch / fonts at the
bottom the big social media buttons. Probably this area could all be
half the size but I like it.
Typical Components of Web 2.0 Site Design
- Lots of space: Web 2.0 sites tend to have a lot of wide-open space. It's a contrast from the 90s, where the trend was to make usage of every square inch of a website's home page with links, banners and applets. White space is embraced to a major degree, as it calls attention to important buttons and links.
- The "Less Is More" Mentality: By putting less on the page, you're drawing more attention to the elements that matter: content and call-to-action buttons. "Clutter" and Web 2.0 simply do not mix - this is a new era of design psychology.
- Gradients: Merely a design element, gradients are used in Web 2.0 site design to give a clean, soft impression that's easy on the eyes.
- Large Fonts: Huge headings are a popular trend in Web 2.0 design - headings are usually taglines that describe or summarize what a website is about in just a handful of words. It's a huge benefit to first-timer usability, especially since new visitors would like to "get to the point" without having to read an intro paragraph.
- Dramatic Color Contrast: Another typical element seen in Web 2.0 design are bright colors (particularly neon colors) that accent site elements including menus, separator bars and footers. Many sites use this same neon color for their hyperlinks and headings, as well. Sometimes, the contrast between bright neon colors and charcoal or light gray text are put in unison for a dramatic effect.
- Eye Candy Logos: In Web 2.0 logo design, it's almost expected to see logos have a shiny plastic luster, or a soft gradient. Most Web 2.0 fonts are similar to basic Arial, Tahoma or Helvetica, and are simple. The colors used within the logo are also typically mimicked on other site design pieces to create a sense of uniformity.
- Huge Buttons: Calls to action (buttons that prompt you to "Get More Information," "Download Now," "See A Demo" or "Buy Now") are typically gigantic in Web 2.0 design. They're also attractive, featuring a color that strays away from the rest of the website's schematic. These buttons are typically isolated by a great deal of space, making them very easy to notice.
- Reflections: Product images, screenshots and icons can be seen as having "reflections" underneath them, as if they were standing on top of a new laminate floor. It's a stereotypical design element of Web 2.0.
- Lots of Icons: Web 2.0 icons are always in vector format, which is the standard format created by software such as Adobe Illustrator and Flash. They're attractive and clean looking, and are used to either draw attention to a website's sub-categories, a product's individual features, or anything else that the web designer wanted to help associate for a viewer.
- Exaggerated Web Form Fields: Huge form fields add to usability and draw attention to sign-ups and registrations. Instead of typing in a search, a username or anything else into a tiny web field, Web 2.0 has evolved them into massive interactive boxes with large text that makes things easy to see. For a good example, look at Wobbet.com's huge fields.

```html
<!DOCTYPE html>
<html lang="en">
<head>
<meta charset="utf-8">
<title>Lorwen Bastable – Retail CIO</title>
<link rel="stylesheet" href="https://fonts.googleapis.com/css2?family=Arvo:wght@400;700&family=Open+Sans:wght@400;700&display=swap">
<style>
:root{
  --navy-deep:#081626;
  --navy:#123a63;
  --ink:#0f2f5a;
  --link:#0b4fa8;
  --text:#444;
  --cyan:#1ea3df;
  --soft-blue:#6aa4d6;
  --panel:#dfe7ef;
  --footer:#ececec;
  --white:#fff;
}
*{box-sizing:border-box;margin:0;padding:0}
html,body{width:1200px;height:988px;overflow:hidden}
body{position:relative;background:var(--white);font-family:Arial,"Open Sans",sans-serif;color:var(--text)}
.page{position:relative;width:1200px;height:988px;overflow:hidden}

.masthead{position:absolute;left:0;top:0;width:1200px;height:497px;z-index:2;
  background:
    repeating-linear-gradient(90deg,rgba(120,180,240,0) 0 40px,rgba(120,180,240,.07) 40px 46px,rgba(120,180,240,0) 46px 90px),
    radial-gradient(ellipse 600px 380px at 600px 420px,#2c6fb0 0%,#17487a 45%,transparent 80%),
    linear-gradient(180deg,var(--navy-deep) 0%,var(--navy) 55%,#1b5287 100%);}
.masthead::after{content:"";position:absolute;left:0;right:0;top:119px;height:1px;background:rgba(110,170,230,.45)}

.brand{position:absolute;left:91px;top:14px;color:var(--white);font-family:"Open Sans",Arial,sans-serif;font-weight:700;font-size:42px;line-height:41px}
.brand-role{position:absolute;left:334px;top:68px;color:var(--soft-blue);font-family:"Open Sans",Arial,sans-serif;font-size:27px;letter-spacing:1px}

.social-top{position:absolute;right:148px;top:26px;display:flex;gap:14px}
.social-link{display:flex;align-items:center;gap:5px;color:#cfe0f0;font-size:12px;text-decoration:none}
.social-link .dot{width:14px;height:14px;border-radius:3px;background:#5a8fc2}

.search{position:absolute;left:745px;top:71px;display:flex}
.search-field{width:219px;height:24px;border:1px solid #cfd8e0;background:#fff;font-size:11px;color:#666;padding:4px 10px}
.search-button{width:89px;height:24px;background:linear-gradient(#3cc0f0,var(--cyan));color:#fff;font-weight:700;font-size:15px;text-align:center;line-height:24px}

.panel{position:absolute;border-radius:10px;background:rgba(210,222,235,.55);padding:8px;box-shadow:0 6px 20px rgba(0,0,0,.35)}
.panel-inner{width:100%;height:100%;border-radius:6px;background:linear-gradient(#eef2f6,var(--panel));overflow:hidden;padding:10px 14px;position:relative}
.panel-inner::after{content:"";position:absolute;right:6px;top:10px;width:9px;height:calc(100% - 20px);border-radius:4px;background:linear-gradient(90deg,#a9c3dc,#7ea5ca)}
.panel.back{opacity:.45}
.panel-title{font-family:Arvo,Georgia,serif;color:#4d74a0;font-size:20px;border-bottom:1px solid #b7c6d4;padding-bottom:2px;margin-bottom:8px;white-space:nowrap}
.panel p{font-size:12px;line-height:17px;color:#555}
.interest-list{list-style:none;margin-top:6px}
.interest-list li{font-size:11px;line-height:15px;margin-bottom:4px;padding-left:16px;position:relative;color:#555}
.interest-list li::before{content:"»";position:absolute;left:2px;top:-1px;color:#223;font-weight:700}
.interest-list a{color:var(--link);text-decoration:none}
.tweets p{font-family:"Open Sans",Verdana,sans-serif;font-size:11px;line-height:16px;margin-bottom:8px;color:#666}

.welcome{position:absolute;left:346px;top:190px;width:508px;height:340px;z-index:10;background:var(--white);border-radius:13px;padding:9px;box-shadow:0 12px 22px rgba(0,0,0,.25)}
.welcome-inner{height:100%;border-radius:8px;background:linear-gradient(#f9f9f9,#eeeeee);border:1px solid #e2e2e2;padding:10px 17px}
.welcome h1{font-family:Arvo,Georgia,serif;font-weight:400;font-size:21px;color:var(--ink);border-bottom:1px solid #bbb;padding-bottom:3px;margin-bottom:9px;letter-spacing:.3px}
.welcome p{font-size:12px;line-height:17.4px;color:#444;margin-bottom:8px}
.welcome a{color:var(--link);text-decoration:none}
.dropcap{font-family:Arvo,Georgia,serif;font-size:22px;color:#555}

.stage{position:absolute;left:0;top:497px;width:1200px;height:394px;z-index:1;background:linear-gradient(#c9c9c9 0%,#fff 18%,#fff 100%)}
.word-band{position:absolute;left:81px;top:613px;width:1039px;height:278px;z-index:1;background:linear-gradient(90deg,#eaeaea,#f4f4f4 50%,#e8e8e8)}
.portrait{position:absolute;left:88px;top:540px;width:369px;height:351px;z-index:3;border-radius:40% 40% 0 0/22% 22% 0 0;background:linear-gradient(#c08a66 0%,#a0765a 25%,#1c1c1c 38%,#111 100%)}
.tagline{position:absolute;left:483px;top:667px;width:612px;z-index:3;font-family:Arvo,Georgia,serif;font-size:27px;line-height:38px;color:var(--ink)}

.site-footer{position:absolute;left:0;top:891px;width:1200px;height:97px;z-index:3;background:var(--footer)}
.copyright{position:absolute;left:96px;top:34px;font-size:11px;color:#666}
.find-us{position:absolute;left:845px;top:30px;display:flex;align-items:center;gap:14px}
.find-us-label{font-family:Arvo,Georgia,serif;font-size:15px;color:#444}
.find-us .social-link{color:#1f6fa8;font-size:13px}
.find-us .dot{width:30px;height:30px;background:var(--cyan)}
</style>
</head>
<body>
<div class="page">
  <header class="masthead">
    <div class="brand">Lorwen<br>Bastable</div>
    <div class="brand-role">RETAIL CIO</div>
    <nav class="social-top">
      <a class="social-link" href="#"><span class="dot"></span>Chirpline</a>
      <a class="social-link" href="#"><span class="dot"></span>Linkwell</a>
    </nav>
    <form class="search">
      <div class="search-field">search here</div>
      <div class="search-button">Search</div>
    </form>

    <section class="panel back" style="left:262px;top:146px;width:323px;height:180px">
      <div class="panel-inner"><h2 class="panel-title">Career Timeline</h2></div>
    </section>
    <section class="panel back" style="left:615px;top:146px;width:325px;height:180px">
      <div class="panel-inner"><h2 class="panel-title">Chirpline</h2></div>
    </section>

    <section class="panel" style="left:148px;top:163px;width:420px;height:258px">
      <div class="panel-inner">
        <h2 class="panel-title">CURRENT INTEREST</h2>
        <p>The following is just a general list of upcoming technologies I'm interested in.</p>
        <ul class="interest-list">
          <li><a href="#">Ecommerce</a> – Long time fan, but not done yet</li>
          <li><a href="#">Better Phone</a> – One that I can drive without a keyboard</li>
          <li><a href="#">Social Commerce</a> – Users driving the sales</li>
          <li><a href="#">Social Shopping</a> – Friends driving purchases</li>
          <li><a href="#">Browser based POS</a> – Needs to work with multichannel</li>
          <li><a href="#">Minimalist websites</a> – Highly effective layouts</li>
        </ul>
      </div>
    </section>

    <section class="panel" style="left:646px;top:163px;width:406px;height:258px">
      <div class="panel-inner tweets">
        <h2 class="panel-title">EVENTS IN AUSTRALIA</h2>
        <p>Lorem ipsum dolor sit amet, consectetur adipiscing elit. Vivamus posuere, elit a consequat mi tincidunt quis.</p>
        <p>Nunc vel justo vitae consequat vulputate, sed luctus ipsum eros id lacus. Fusce vitae lorem. Donec rutrum dui et justo.</p>
        <p>Aenean augue, dictum sit amet tincidunt mauris congue lorem condimentum eu.</p>
      </div>
    </section>

    <article class="welcome">
      <div class="welcome-inner">
        <h1>WELCOME TO LORWEN BASTABLE</h1>
        <p><span class="dropcap">H</span>ello, and welcome to my home page on the web. There isn't really much going on here, more just a front end for my webmail etc. For those that are interested in learning a bit more about me <a href="#">personally</a> or <a href="#">commercially</a>, feel free to click around and have a look.</p>
        <p>My background is basically a sales guy who a long time ago learnt how to use technology to reach the masses. After running <a href="#">BBS's</a> for years to support our computer business, I built my first commercial web site around 1994 and quickly moved into full blown <a href="#">eCommerce</a> sites. Did a stint next in <a href="#">Web Marketing</a> and <a href="#">SEO</a> which lead to a couple of years of hammering <a href="#">affiliate programs</a> and <a href="#">Searchly Adpanel</a> across the web.</p>
        <p>In 2007 I went back into mainstream retail as the <a href="#">CIO</a> of <a href="#">Marlow Bean Coffees</a> one of Australias largest franchises. In 2010 looking for a new challenge I joined <a href="#">Vantell</a> in their newly created role as head of Retail Technology.</p>
      </div>
    </article>
  </header>

  <section class="stage"></section>
  <div class="word-band" role="img" aria-label="Faint typographic texture of stacked words about books and information"></div>
  <div class="portrait" role="img" aria-label="Portrait photo of Lorwen Bastable in a dark shirt"></div>
  <p class="tagline">Retail CIO with a passion for multi-channel, multi-store technology.Specialise in using online communities to help drive the business by consumer engagement...</p>

  <footer class="site-footer">
    <p class="copyright">Copyright © 2011 Lorwen Bastable</p>
    <div class="find-us">
      <span class="find-us-label">Find us on:</span>
      <a class="social-link" href="#"><span class="dot"></span>Chirpline</a>
      <a class="social-link" href="#"><span class="dot"></span>Linkwell</a>
    </div>
  </footer>
</div>
</body>
</html>
```